GRHWC 2026 Theme for Wall Banners

We need a design created for a wall banner 4 x 4 feet, for our church's 2026 Theme:
"Applying God's Word"
"Acquiring God's Wisdom"
"Acknowledging God's Will"
"Advancing God's Work"
Proverbs 3:5-6

Use the church's colors purple, silver, white and include the logo
Church Name: Grace-Rooted Harvest Church of Willow Creek

Target Market(s)

Male & Female, ages 0-99

Industry/Entity Type

Religious, church

Colors
6B429C
8869AF
B7A5CE
E3DAEB
F3F0F8

Requirements
Must have
• Logo, colors, use of all 4 phrases; use of scripture text
Nice to have
• Maybe the phrases in / on pillars
Should not have
• Images or language that is non-Christian

```html
<!DOCTYPE html>
<html lang="en">
<head>
<meta charset="utf-8">
<title>GRHWC 2026 Theme Wall Banner</title>
<link rel="stylesheet" href="https://fonts.googleapis.com/css2?family=Fira+Sans+Extra+Condensed:ital,wght@0,300;0,600;1,300;1,800&family=Yellowtail&family=Arimo&display=swap">
<style>
  :root {
    --page-bg: #e4e4e6;
    --purple-deep: #3b2a8e;
    --purple-mid: #4a3699;
    --purple-soft: #6b5aaa;
    --lavender: #8869af;
    --silver: #c9c6d3;
    --white: #ffffff;
  }
  html, body {
    margin: 0;
    width: 1200px;
    height: 900px;
    overflow: hidden;
    background: var(--page-bg);
  }
  .banner {
    position: absolute;
    left: 190px;
    top: 40px;
    width: 820px;
    height: 820px;
    box-shadow: 0 10px 30px rgba(0,0,0,0.18);
  }
  .banner svg { display: block; }
  .church-mark {
    font-family: "Fira Sans Extra Condensed", sans-serif;
    font-weight: 600;
    font-size: 46px;
    fill: var(--white);
    letter-spacing: 2px;
  }
  .church-name {
    font-family: "Fira Sans Extra Condensed", sans-serif;
    font-style: italic;
    font-weight: 300;
    font-size: 36px;
    fill: var(--white);
  }
  .theme-verb {
    font-family: "Yellowtail", cursive;
    fill: var(--white);
  }
  .theme-object {
    font-family: "Fira Sans Extra Condensed", sans-serif;
    font-style: italic;
    font-weight: 800;
    fill: var(--white);
  }
  .scripture-ref {
    font-family: "Arimo", sans-serif;
    font-size: 30px;
    fill: var(--white);
  }
  .frame-corner {
    fill: none;
    stroke: var(--white);
    stroke-width: 2;
  }
</style>
</head>
<body>
<main class="banner">
  <svg width="820" height="820" viewBox="0 0 820 820" xmlns="http://www.w3.org/2000/svg">
    <defs>
      <linearGradient id="banner-tone" x1="0" y1="0" x2="1" y2="1">
        <stop offset="0" stop-color="#3e2c8f"/>
        <stop offset="0.55" stop-color="#4a3699"/>
        <stop offset="1" stop-color="#3f2e92"/>
      </linearGradient>
      <radialGradient id="banner-glow" cx="0.05" cy="0.85" r="0.55">
        <stop offset="0" stop-color="#8a82bd" stop-opacity="0.9"/>
        <stop offset="1" stop-color="#8a82bd" stop-opacity="0"/>
      </radialGradient>
      <radialGradient id="banner-glow-top" cx="0.95" cy="0.05" r="0.5">
        <stop offset="0" stop-color="#6d63b3" stop-opacity="0.8"/>
        <stop offset="1" stop-color="#6d63b3" stop-opacity="0"/>
      </radialGradient>
    </defs>

    <g class="banner-background" role="img" aria-label="Purple-tinted photograph of hands folded in prayer">
      <rect width="820" height="820" fill="url(#banner-tone)"/>
      <rect width="820" height="820" fill="url(#banner-glow)"/>
      <rect width="820" height="820" fill="url(#banner-glow-top)"/>
    </g>

    <g class="church-logo">
      <circle cx="318" cy="110" r="22" fill="var(--silver)"/>
      <text class="church-mark" x="352" y="127">GRHWC</text>
    </g>

    <text class="church-name" x="410" y="251" text-anchor="middle">Grace-Rooted Harvest Church of Willow Creek</text>

    <path class="frame-corner" d="M32 345 V311 H66"/>
    <path class="frame-corner" d="M754 311 H788 V345"/>
    <path class="frame-corner" d="M32 735 V769 H66"/>
    <path class="frame-corner" d="M754 769 H788 V735"/>

    <g class="theme-phrase">
      <text class="theme-verb" x="60" y="381" font-size="66" textLength="282" lengthAdjust="spacingAndGlyphs">Applying</text>
      <text class="theme-object" x="79" y="450" font-size="80" textLength="321" lengthAdjust="spacingAndGlyphs">God's Word</text>
    </g>
    <g class="theme-phrase">
      <text class="theme-verb" x="418" y="471" font-size="66" textLength="358" lengthAdjust="spacingAndGlyphs">Acquiring</text>
      <text class="theme-object" x="446" y="527" font-size="58" textLength="270" lengthAdjust="spacingAndGlyphs">God's Wisdom</text>
    </g>
    <g class="theme-phrase">
      <text class="theme-verb" x="43" y="561" font-size="60" textLength="378" lengthAdjust="spacingAndGlyphs">Acknowledging</text>
      <text class="theme-object" x="79" y="617" font-size="66" textLength="220" lengthAdjust="spacingAndGlyphs">God's Will</text>
    </g>
    <g class="theme-phrase">
      <text class="theme-verb" x="358" y="668" font-size="66" textLength="388" lengthAdjust="spacingAndGlyphs">Advancing</text>
      <text class="theme-object" x="386" y="735" font-size="76" textLength="290" lengthAdjust="spacingAndGlyphs">God's Work</text>
    </g>

    <text class="scripture-ref" x="80" y="772">Proverbs 3:5-6</text>
  </svg>
</main>
</body>
</html>
```